BRIGHTDESK COWORKING Website design and coding

BRIGHTDESK COWORKING

BRIGHTDESK is Galveston’s first (and currently only) shared business co-working space. We share the same upscale, casual work environment, but we work independently on our own (or our team’s) projects and goals. For only a flat $195 membership fee per month, you have your very own all-inclusive, fun, personal business office environment. Website is written (Word file #12, below); and all pictures etc provided. Galveston is a beachy, coastal, historic city an hour from Houston, Texas USA. Logo (file 11 below) is temporary only.

Target Market(s)

Outside sales people, medical students looking for study hall, Houston companies looking for local office, real estate agents, graphic artists, entrepreneurs, etc

Contact Information for Business Card

will discuss --want to combine with current business card with multiple businesses

Logo Text

BRIGHTDESK COWORKING

Coding

Coded - Design and coding required

Number of Pages Required

5+ page

Colors
ec1f27
fbed22

Requirements
Nice to have
• maroon/wine dominant with yellow and red accents, gray base are the colors of the space--website could coordinate--but open to creative ideas/combinations

```html
<!DOCTYPE html>
<html lang="en">
<head>
<meta charset="utf-8">
<title>BrightDesk Coworking – The BrightDesk Pilosophy</title>
<link href="https://fonts.googleapis.com/css2?family=Montserrat:wght@400;500;600;700&display=swap" rel="stylesheet">
<style>
  :root {
    --red: #d0111b;
    --yellow: #fbed22;
    --ink: #111111;
    --white: #ffffff;
    --photo-warm-a: #c9b26a;
    --photo-warm-b: #3a2f24;
    --photo-kitchen-a: #d8d2b8;
    --photo-kitchen-b: #5a3040;
  }
  * { box-sizing: border-box; margin: 0; padding: 0; }
  html, body { width: 1200px; height: 2635px; overflow: hidden; background: var(--white); }
  body { position: relative; font-family: "Montserrat", sans-serif; color: var(--ink); }
  .abs { position: absolute; }

  .site-header { position: absolute; left: 0; top: 0; width: 1200px; height: 78px; background: var(--white); }
  .brand { position: absolute; left: 135px; top: 18px; font-size: 30px; font-weight: 700; color: #666; letter-spacing: -0.5px; }
  .nav { position: absolute; top: 27px; font-size: 13px; font-weight: 600; list-style: none; }
  .nav li { position: absolute; white-space: nowrap; }
  .nav .active { color: var(--red); }

  .photo { position: absolute; }
  .photo.warm { background: linear-gradient(160deg, var(--photo-warm-a) 0%, #8a7a55 45%, var(--photo-warm-b) 100%); }
  .photo.kitchen { background: linear-gradient(120deg, #6f6a62 0%, var(--photo-kitchen-a) 45%, var(--photo-kitchen-b) 100%); }

  .page-title { position: absolute; left: 139px; top: 257px; width: 635px; height: 114px; background: var(--yellow); border-left: 8px solid var(--red); }
  .page-title h1 { position: absolute; left: 22px; top: 36px; font-size: 28px; font-weight: 600; }

  .card { position: absolute; width: 550px; background: var(--yellow); padding: 0 38px 0 34px; }
  .card h2 { font-size: 13px; font-weight: 600; margin-bottom: 14px; }
  .card p { font-size: 13px; line-height: 16px; font-weight: 400; }
  .marker { position: absolute; width: 43px; height: 53px; background: var(--red); }

  .cta { position: absolute; left: 143px; top: 2302px; width: 907px; height: 153px; background: linear-gradient(90deg, #a39a3a 0%, #d8cc7a 45%, #bfb25a 100%); }
  .cta h3 { position: absolute; right: 24px; top: 28px; font-size: 27px; font-weight: 600; }
  .cta .join { position: absolute; left: 707px; top: 77px; width: 170px; height: 42px; background: var(--red); color: var(--white); font-size: 13px; font-weight: 600; text-align: center; line-height: 42px; }

  .site-footer { position: absolute; left: 0; top: 2496px; width: 1200px; height: 118px; background: var(--red); color: var(--white); }
  .site-footer .brand { color: var(--white); top: 16px; }
  .site-footer .nav { top: 31px; }
  .address { position: absolute; left: 136px; top: 56px; font-size: 13px; line-height: 16px; font-weight: 500; }
  .copyright { position: absolute; left: 0; top: 2614px; width: 1200px; height: 21px; background: var(--yellow); font-size: 11px; font-weight: 600; padding-left: 136px; line-height: 21px; }
</style>
</head>
<body>

<header class="site-header">
  <div class="brand">BrightDesk</div>
  <ul class="nav">
    <li style="left:424px">ABOUT</li>
    <li style="left:489px">AMENITIES</li>
    <li style="left:583px">MEMBERSHIP</li>
    <li style="left:701px">PICTURES</li>
    <li style="left:792px" class="active">THE BRIGHTDESK PILOSOPHY</li>
    <li style="left:997px">CONTACT</li>
  </ul>
</header>

<div class="photo kitchen" style="left:0;top:78px;width:1200px;height:238px" role="img" aria-label="Coworking kitchen with vessel sink, steel fridge and bar counter with stools"></div>
<div class="page-title"><h1>THE BRIGHTDESK PILOSOPHY</h1></div>

<section>
  <div class="photo warm" style="left:136px;top:430px;width:549px;height:415px" role="img" aria-label="Open lounge with sofas, gaming chairs and glass office partitions"></div>
  <div class="card" style="left:509px;top:576px;height:198px;padding-top:18px">
    <h2>WORK OUTSIDE THE HOME</h2>
    <p>Free yourself for the burdens of house or school, and work in an environment that MOTIVATES you instead of DISTRACTS you.&nbsp; Meet like-minded people that can help you along, and yet you have the option to work in a quiet-and very comfortable – private office cubicle.&nbsp; Perfect for medical students, entrepreneurs, designers, writers, business reps away from headquarters, contractors working on bids or plans, or anyone needing a flexible, fun business environment!</p>
  </div>
  <div class="marker" style="left:489px;top:558px"></div>
</section>

<section>
  <div class="photo kitchen" style="left:506px;top:885px;width:549px;height:416px" role="img" aria-label="Shared kitchen with refrigerator, pendant lights and bar seating"></div>
  <div class="card" style="left:151px;top:1058px;height:142px;padding-top:28px">
    <h2>BRIGHTDESK THE COMPETITION</h2>
    <p>Because of the flexibility, prestigious location, opportunities to meet and network with active professionals, and the available tech and amenities, you have all the tools you need to excel in your chosen field.</p>
  </div>
  <div class="marker" style="left:135px;top:1040px"></div>
</section>

<section>
  <div class="photo warm" style="left:136px;top:1352px;width:549px;height:416px" role="img" aria-label="Long shared worktables under pendant lamps with chairs"></div>
  <div class="card" style="left:509px;top:1500px;height:197px;padding-top:38px">
    <h2>WORK IT OUT WITH YOUR COWORKERS.</h2>
    <p>BRIGHTDESK is a community – if you are making a pot of (free) coffee – ask and make enough for everyone that wants some!&nbsp; You rapidly become part of more than an office – you have new friends, teachers, people you can trade skills and your experience with!&nbsp; If you have a partner or employee in your own business, a membership for him/her allows you to work alongside each other.</p>
  </div>
  <div class="marker" style="left:492px;top:1481px"></div>
</section>

<section>
  <div class="photo warm" style="left:506px;top:1822px;width:549px;height:416px" role="img" aria-label="Lounge area with black leather sofas and glass office doors"></div>
  <div class="card" style="left:149px;top:1970px;height:196px;padding-top:54px">
    <h2>WORK OUT THE PATH TO YOUR SUCCESS</h2>
    <p>As your business grows, there are other beautiful, “dedicated desk” private executive offices, and full office suites available in the building.&nbsp; Meet your coworkers and synergize with their energy and experience to jump–start your own career.</p>
  </div>
  <div class="marker" style="left:137px;top:1943px"></div>
</section>

<section class="cta" role="img" aria-label="Counter with potted plant in warm yellow light">
  <h3>GET A FREE DAY, TO TRY US</h3>
  <div class="join">JOIN UR MEMBER</div>
</section>

<footer class="site-footer">
  <div class="brand">BrightDesk</div>
  <ul class="nav">
    <li style="left:424px">ABOUT</li>
    <li style="left:489px">AMENITIES</li>
    <li style="left:584px">MEMBERSHIP</li>
    <li style="left:702px">PICTURES</li>
    <li style="left:793px">THE BRIGHTDESK PILOSOPHY</li>
    <li style="left:998px">CONTACT</li>
  </ul>
  <address class="address" style="font-style:normal">Brightdesk Coworking<br>480 Harbor Lane, Suite 12<br>Bayview, TX 77000</address>
</footer>
<div class="copyright">Copyright 2020 BRIGHTDESK COWORKING</div>

</body>
</html>
```